Valkemo App for Smart Devices IoT WiFi Electronic

Valkemo is a siren manufacturer. This application is used for the company's products that have a Wi-Fi connection and an internet connection, which can be configured and activated remotely through this application. In addition, this application is used to activate the siren at specific times for the start and end of shifts in companies and schools. Users will be siren installers and IT or HR managers.
In addition to activating motorized sirens timers, some siren models have speakers and allow you to play TTS (text to speech) audio, audio recorded by the user on the phone and upload audio (mp3) with playlist programming with start and end times.
Application screens: home with dashboard (one dashboard for each category). Device categories: timers, speakers, motorized siren. Screen for requesting evaluation in the App Market. Screen for registering the user profile. Screen for registering devices according to their category (timers, speakers, motorized siren). Screen for registering device groups. Screen for pairing the device on the client's Wi-Fi network. Screen for registering activation times. Screen for uploading MP3 audios. Screen for registering playlists with audio selection, start and end times. Screen for recording audio for later sending to the speakers. Screen for converting text to speech and sending to the speakers. It is important to have a time picker with the day of the week to program the activation times and playlist.

Target Market(s)

Schools, Companies and Stores.

Industry/Entity Type

IoT

Font styles to use
Sans Serif
Other font styles liked:
• roboto

Colors
FFC000
F8CF3A
FAE287
FDF2CF
FEFAEE

Requirements
Must have
• time picker with weekdays for timer programming feature.
Nice to have
• app review request screen on App Market

```html
<!DOCTYPE html>
<html lang="en">
<head>
<meta charset="utf-8">
<title>Valkemo App Screens</title>
<link href="https://fonts.googleapis.com/css2?family=Rubik:wght@400;500;600;700&display=swap" rel="stylesheet">
<style>
:root{
  --yellow:#FFC000;
  --yellow-2:#F8CF3A;
  --yellow-3:#FAE287;
  --yellow-4:#FDF2CF;
  --cream:#FEFAEE;
  --bg:#1f1f1f;
  --ink:#111;
  --grey:#6f6f6f;
  --grey-light:#b9b9b9;
  --nav-grey:#d9d9d9;
  --red:#e8141c;
}
*{box-sizing:border-box;margin:0;padding:0}
html,body{width:1151px;height:1200px;overflow:hidden;background:var(--bg);font-family:"Rubik",sans-serif}
.board{position:absolute;left:0;top:0;width:1720px;height:1794px;transform:scale(0.66919);transform-origin:0 0}
.screen{position:absolute;width:320px;height:568px;background:#fff;overflow:hidden}
.abs{position:absolute}
.title{position:absolute;left:18px;top:16px;font-size:20px;font-weight:500;color:var(--grey);display:flex;align-items:center;gap:14px}
.title svg{width:14px;height:14px}
.brand{position:absolute;left:0;right:0;text-align:center;color:var(--yellow);font-weight:500}
.heading{position:absolute;left:0;right:0;text-align:center;font-weight:600;font-size:23px;color:var(--ink)}
.field{position:absolute;left:25px;width:270px;height:42px;border:1.5px solid var(--yellow);border-radius:7px;font-size:13px;color:var(--grey-light);padding-left:19px;display:flex;align-items:center;justify-content:space-between;padding-right:18px}
.btn{position:absolute;height:42px;background:var(--yellow);color:#fff;border-radius:7px;font-size:13px;font-weight:500;display:flex;align-items:center;justify-content:center}
.nav{position:absolute;left:0;bottom:0;width:320px;height:78px;background:#fff;border-radius:16px 16px 0 0;box-shadow:0 -4px 10px rgba(0,0,0,.05);display:flex;justify-content:space-around;padding:12px 12px 0}
.nav-item{display:flex;flex-direction:column;align-items:center;width:90px;font-size:13px;color:var(--nav-grey)}
.nav-item i{width:38px;height:38px;border-radius:50%;background:var(--nav-grey);margin-bottom:5px}
.nav-item.active{color:var(--yellow);font-weight:500}
.nav-item.active i{background:var(--yellow)}
.banner{position:absolute;left:23px;top:69px;width:275px;height:117px;background:var(--yellow);border-radius:14px;overflow:hidden}
.banner h2{position:absolute;left:12px;top:48px;color:#fff;font-size:22px;font-weight:600}
.banner-photo{position:absolute;left:144px;top:22px;width:118px;height:118px;border-radius:50%;background:var(--yellow-4);color:var(--yellow);display:flex;flex-direction:column;align-items:center;padding-top:46px;font-size:12px;font-weight:500}
.banner-photo small{font-size:7px;font-weight:400}
.section{position:absolute;left:23px;font-size:19px;font-weight:600;color:var(--ink)}
.card{position:absolute;width:130px;height:72px;background:#fff;border-radius:8px;box-shadow:0 2px 8px rgba(0,0,0,.08);overflow:hidden;font-size:13px;color:var(--ink);padding:12px}
.card-img{position:absolute;right:8px;top:27px;width:58px;height:58px;border-radius:50%;background:var(--yellow);color:var(--yellow-4);font-size:8px;text-align:center;padding-top:22px;line-height:1}
.card-img small{display:block;font-size:4px}
.row{position:absolute;left:7px;width:304px;height:68px;border-bottom:1px solid #e4e4e4;display:flex;align-items:center;padding:0 18px 0 15px;font-size:13px;color:var(--ink)}
.row .file-icon{width:32px;height:32px;background:var(--yellow);border-radius:4px;margin-right:12px}
.row .time{margin-left:auto}
.tile{position:absolute;width:100px;text-align:center;font-size:13px;color:var(--ink)}
.tile .art{width:100px;height:100px;background:var(--yellow);margin-bottom:9px}
.tile b{font-weight:500}
.picker{position:absolute;left:0;width:320px;font-weight:500}
.picker span{position:absolute;text-align:center}
.weekdays{position:absolute;left:22px;top:298px;width:276px;display:flex;justify-content:space-between}
.weekdays span{width:32px;height:32px;border-radius:50%;border:1.5px solid var(--yellow);color:var(--yellow);font-size:12px;font-weight:500;display:flex;align-items:center;justify-content:center}
.weekdays span.on{background:var(--yellow);color:#fff}
.caption{position:absolute;left:0;right:0;text-align:center;font-size:10px;color:var(--ink)}
.round-btn{position:absolute;width:60px;height:60px;border-radius:50%;background:#fff;box-shadow:0 3px 10px rgba(0,0,0,.12);display:flex;align-items:center;justify-content:center}
.dim{position:absolute;inset:0;background:rgba(40,40,40,.62)}
.dialog{position:absolute;left:45px;top:200px;width:230px;height:168px;background:#fff;border-radius:12px;text-align:center;padding-top:22px}
.dialog h3{font-size:12px;font-weight:600;line-height:1.3;color:var(--ink)}
.dialog p{font-size:6.5px;font-style:italic;color:#444;line-height:1.8;margin:6px 16px 0}
.stars{color:var(--yellow);font-size:28px;letter-spacing:4px;margin-top:4px}
</style>
</head>
<body>
<div class="board">

<!-- Splash -->
<section class="screen splash" style="left:30px;top:30px;background:#f8f6f3">
  <svg class="abs" style="left:0;top:120px" width="320" height="320" viewBox="0 0 320 320" fill="none" stroke="#ece8e2">
    <circle cx="160" cy="160" r="160"/><circle cx="160" cy="160" r="102"/><circle cx="160" cy="160" r="58"/>
  </svg>
  <div class="brand" style="top:250px;font-size:50px">valkemo</div>
</section>

<!-- Home -->
<section class="screen home" style="left:365px;top:30px">
  <svg class="abs" style="left:20px;top:22px" width="18" height="18" viewBox="0 0 18 18" fill="none" stroke="var(--red)" stroke-width="2.2"><path d="M7 2h8v14H7M2 9h9M8 5l3 4-3 4"/></svg>
  <svg class="abs" style="left:284px;top:24px" width="14" height="14" viewBox="0 0 14 14" fill="none" stroke="#999" stroke-width="2"><path d="M2 4a8 8 0 0 1 8 8M2 8a4 4 0 0 1 4 4"/><circle cx="2.5" cy="11.5" r="1.3" fill="#999"/></svg>
  <div class="banner"><h2>Hi Hana!</h2><div class="banner-photo" role="img" aria-label="User profile photo">Image Here<small>To be Updated</small></div></div>
  <div class="section" style="top:218px">Devices</div>
  <div class="card" style="left:23px;top:252px">Timers<div class="card-img" role="img" aria-label="Timer device photo">Device IMG<small>To be Updated</small></div></div>
  <div class="card" style="left:169px;top:252px">Speakers<div class="card-img" role="img" aria-label="Speaker device photo">Device IMG<small>To be Updated</small></div></div>
  <div class="card" style="left:23px;top:343px;line-height:1.25">Motorized<br>Sirens<div class="card-img" role="img" aria-label="Motorized siren photo">Device IMG<small>To be Updated</small></div></div>
  <nav class="nav"><div class="nav-item active"><i></i>Home</div><div class="nav-item"><i></i>Add Device</div><div class="nav-item"><i></i>Music</div></nav>
</section>

<!-- Login -->
<section class="screen login" style="left:700px;top:30px">
  <div class="brand" style="top:80px;font-size:19px">valkemo</div>
  <div class="heading" style="top:148px">LOGIN</div>
  <div class="field" style="top:196px">Email Address</div>
  <div class="field" style="top:256px">Password</div>
  <div class="btn" style="left:112px;top:330px;width:97px">Login</div>
</section>

<!-- Register -->
<section class="screen register" style="left:1035px;top:30px">
  <div class="brand" style="top:80px;font-size:19px">valkemo</div>
  <div class="heading" style="top:128px">REGISTER</div>
  <div class="field" style="top:184px">Full Name</div>
  <div class="field" style="top:244px">Email Address</div>
  <div class="field" style="top:304px">Organization</div>
  <div class="field" style="top:364px">Password</div>
  <div class="btn" style="left:79px;top:438px;width:163px">Create Account</div>
</section>

<!-- Add Device (with device group) -->
<section class="screen add-device" style="left:1370px;top:30px">
  <div class="title">Add Device</div>
  <div class="abs" role="img" aria-label="Device photo" style="left:95px;top:62px;width:130px;height:130px;background:var(--yellow);border-radius:14px;color:var(--yellow-4);text-align:center;padding-top:48px;font-size:17px;font-weight:500">Device Image<div style="font-size:9px;font-weight:400">To be Updated</div></div>
  <div class="field" style="top:208px">Set Device Name</div>
  <div class="field" style="top:260px">Select Device Type<svg width="16" height="10" viewBox="0 0 16 10" fill="none" stroke="var(--yellow)" stroke-width="2"><path d="M1 1l7 7 7-7"/></svg></div>
  <div class="field" style="top:312px">Select Device Group<svg width="16" height="10" viewBox="0 0 16 10" fill="none" stroke="var(--yellow)" stroke-width="2"><path d="M1 1l7 7 7-7"/></svg></div>
  <div class="field" style="top:364px">Device Address<svg width="16" height="10" viewBox="0 0 16 10" fill="none" stroke="var(--yellow)" stroke-width="2"><path d="M1 1l7 7 7-7"/></svg></div>
  <div class="btn" style="left:25px;top:424px;width:270px">Add Device</div>
  <nav class="nav"><div class="nav-item"><i></i>Home</div><div class="nav-item active"><i></i>Add Device</div><div class="nav-item"><i></i>Music</div></nav>
</section>

<!-- Set Time -->
<section class="screen set-time" style="left:30px;top:613px">
  <div class="title"><svg viewBox="0 0 14 14" fill="none" stroke="#666" stroke-width="2"><path d="M10 1L4 7l6 6"/></svg>Set Time</div>
  <div class="picker" style="top:146px;font-size:32px;color:var(--yellow-3)"><span style="left:55px">07</span><span style="left:139px">29</span></div>
  <div class="picker" style="top:190px;font-size:37px;color:var(--yellow)"><span style="left:50px">08</span><span style="left:110px">:</span><span style="left:134px">30</span><span style="left:212px">AM</span></div>
  <div class="picker" style="top:238px;font-size:32px;color:var(--yellow-3)"><span style="left:55px">09</span><span style="left:142px">31</span><span style="left:212px">PM</span></div>
  <div class="weekdays"><span class="on">M</span><span class="on">T</span><span class="on">W</span><span class="on">T</span><span class="on">F</span><span>S</span><span>S</span></div>
  <div class="abs" style="left:22px;top:361px;width:122px;height:54px;background:var(--yellow);border-radius:7px;display:flex;align-items:center;padding-left:14px;gap:12px;color:#fff;font-size:13px;font-weight:500;line-height:1.2"><i style="width:28px;height:28px;border-radius:50%;background:#fff"></i><span>Set<br>Music</span></div>
  <div class="abs" style="left:166px;top:361px;width:132px;height:54px;border:1.5px solid var(--yellow);border-radius:7px;display:flex;align-items:center;padding-left:14px;gap:12px;color:var(--yellow);font-size:13px;font-weight:500;line-height:1.2"><i style="width:28px;height:28px;border-radius:50%;background:var(--yellow)"></i><span>Set<br>Playlist</span></div>
</section>

<!-- Set MP3 -->
<section class="screen set-mp3" style="left:365px;top:613px">
  <div class="title"><svg viewBox="0 0 14 14" fill="none" stroke="#666" stroke-width="2"><path d="M10 1L4 7l6 6"/></svg>Set MP3</div>
  <div class="abs" style="left:7px;top:55px;width:304px;border-top:1px solid #e4e4e4"></div>
  <div class="row" style="top:56px"><i class="file-icon"></i>MP3 File Name<span class="time">00:00:05</span></div>
  <div class="row" style="top:124px"><i class="file-icon"></i>MP3 File Name<span class="time">00:00:05</span></div>
  <div class="row" style="top:192px"><i class="file-icon"></i>MP3 File Name<span class="time">00:00:05</span></div>
  <div class="row" style="top:260px"><i class="file-icon"></i>MP3 File Name<span class="time">00:00:05</span></div>
  <div class="row" style="top:328px"><i class="file-icon"></i>MP3 File Name<span class="time">00:00:05</span></div>
  <div class="row" style="top:396px"><i class="file-icon"></i>MP3 File Name<span class="time">00:00:05</span></div>
</section>

<!-- Pairing -->
<section class="screen pairing" style="left:700px;top:613px">
  <div class="title"><svg viewBox="0 0 14 14" fill="none" stroke="#666" stroke-width="2"><path d="M10 1L4 7l6 6"/></svg>Pairing</div>
  <svg class="abs" style="left:0;top:0" width="320" height="568" viewBox="0 0 320 568" fill="none">
    <g stroke="#ececec"><circle cx="160" cy="284" r="130"/><circle cx="160" cy="284" r="104"/><circle cx="160" cy="284" r="72"/></g>
    <g stroke="#999" stroke-width="5" stroke-linecap="round"><path d="M146 270a28 28 0 0 1 28 28M146 282a16 16 0 0 1 16 16"/></g>
    <circle cx="148" cy="295" r="4" fill="#999"/>
    <circle cx="275" cy="222" r="11" fill="var(--yellow)"/><circle cx="68" cy="328" r="11" fill="var(--yellow)"/>
  </svg>
  <div class="abs" style="left:250px;top:237px;font-size:9px;text-align:center;line-height:1.25">Device<br>Name 2</div>
  <div class="abs" style="left:43px;top:343px;font-size:9px;text-align:center;line-height:1.25">Device<br>Name 1</div>
  <div class="caption" style="top:446px">2 Users Found</div>
  <div class="caption" style="top:514px;font-size:13px;font-weight:500">Wifi Name</div>
</section>

<!-- Set Playlist -->
<section class="screen set-playlist" style="left:1035px;top:613px">
  <div class="title"><svg viewBox="0 0 14 14" fill="none" stroke="#666" stroke-width="2"><path d="M10 1L4 7l6 6"/></svg>Set Playlist</div>
  <div class="tile" style="left:40px;top:89px"><div class="art"></div><b>+ Create New</b></div>
  <div class="tile" style="left:181px;top:89px"><div class="art"></div>Playlist Name</div>
  <div class="tile" style="left:40px;top:251px"><div class="art"></div>Playlist Name</div>
</section>

<!-- Audio Recorder -->
<section class="screen recorder" style="left:1370px;top:613px">
  <div class="title"><svg viewBox="0 0 14 14" fill="none" stroke="#666" stroke-width="2"><path d="M10 1L4 7l6 6"/></svg>Audio Recorder</div>
  <div class="abs" role="img" aria-label="Audio waveform" style="left:34px;top:235px;width:250px;height:88px;background:var(--yellow);border-radius:8px;color:var(--yellow-4);text-align:center;padding-top:28px;font-size:19px;font-weight:500">Wavelength Image<div style="font-size:9px;font-weight:400">To be Updated</div></div>
  <div class="caption" style="top:450px">Press to start recording</div>
  <div class="round-btn" style="left:130px;top:475px"><i style="width:30px;height:30px;border-radius:50%;background:var(--red)"></i></div>
</section>

<!-- Manage MP3 -->
<section class="screen manage-mp3" style="left:30px;top:1196px">
  <div class="title"><svg viewBox="0 0 14 14" fill="none" stroke="#666" stroke-width="2"><path d="M10 1L4 7l6 6"/></svg>Manage MP3</div>
  <svg class="abs" style="left:279px;top:22px" width="18" height="18" viewBox="0 0 18 18" fill="none" stroke="var(--yellow)" stroke-width="2"><path d="M2 10v6h14v-6M9 2v10M5 8l4 4 4-4"/></svg>
  <div class="abs" style="left:7px;top:55px;width:304px;border-top:1px solid #e4e4e4"></div>
  <div class="row" style="top:56px"><i class="file-icon"></i>MP3 File Name<span class="time">00:00:05</span></div>
  <div class="row" style="top:124px"><i class="file-icon"></i>MP3 File Name<span class="time">00:00:05</span></div>
  <div class="row" style="top:192px"><i class="file-icon"></i>MP3 File Name<span class="time">00:00:05</span></div>
  <div class="row" style="top:260px"><i class="file-icon"></i>MP3 File Name<span class="time">00:00:05</span></div>
  <div class="row" style="top:328px"><i class="file-icon"></i>MP3 File Name<span class="time">00:00:05</span></div>
  <div class="row" style="top:396px;border-bottom:none"><i class="file-icon"></i>MP3 File Name<span class="time">00:00:05</span></div>
</section>

<!-- Text to Speech -->
<section class="screen tts" style="left:365px;top:1196px">
  <div class="title"><svg viewBox="0 0 14 14" fill="none" stroke="#666" stroke-width="2"><path d="M10 1L4 7l6 6"/></svg>Text to Speech</div>
  <div class="abs" style="left:25px;top:63px;width:270px;height:310px;border:1.5px solid var(--yellow);border-radius:14px;font-size:13px;color:var(--grey-light);padding:20px 22px">Type your message here</div>
  <div class="abs" style="left:150px;top:338px;font-size:9px;text-align:right;line-height:1.3;color:var(--ink)">Review how it<br>sounds like</div>
  <i class="abs" style="left:253px;top:338px;width:22px;height:22px;border-radius:50%;background:var(--yellow)"></i>
  <div class="field" style="top:384px">Select a voice to use<svg width="16" height="10" viewBox="0 0 16 10" fill="none" stroke="var(--yellow)" stroke-width="2"><path d="M1 1l7 7 7-7"/></svg></div>
  <div class="caption" style="top:450px">Press to publicize the message</div>
  <div class="round-btn" style="left:130px;top:475px"><svg width="26" height="28" viewBox="0 0 26 28"><path d="M2 1l23 13L2 27z" fill="var(--yellow)"/></svg></div>
</section>

<!-- Review request -->
<section class="screen review" style="left:700px;top:1196px">
  <svg class="abs" style="left:20px;top:22px" width="18" height="18" viewBox="0 0 18 18" fill="none" stroke="var(--red)" stroke-width="2.2"><path d="M7 2h8v14H7M2 9h9M8 5l3 4-3 4"/></svg>
  <svg class="abs" style="left:284px;top:24px" width="14" height="14" viewBox="0 0 14 14" fill="none" stroke="#999" stroke-width="2"><path d="M2 4a8 8 0 0 1 8 8M2 8a4 4 0 0 1 4 4"/><circle cx="2.5" cy="11.5" r="1.3" fill="#999"/></svg>
  <div class="banner"><h2>Hi Hana!</h2><div class="banner-photo" role="img" aria-label="User profile photo"></div></div>
  <div class="section" style="top:218px">Devices</div>
  <div class="card" style="left:23px;top:252px">Timers<div class="card-img"></div></div>
  <div class="card" style="left:169px;top:252px">Speakers<div class="card-img"></div></div>
  <div class="card" style="left:23px;top:343px;line-height:1.25">Motorized<br>Sirens<div class="card-img"></div></div>
  <div class="dim"></div>
  <div class="dialog">
    <h3>Enjoying Valkemo?<br>We’d love to hear from you!</h3>
    <p>Your feedback helps us improve and provide the best experience possible. If you’re finding our app helpful, please take a moment to rate us on the App Market!</p>
    <div class="stars">★★★★★</div>
  </div>
  <svg class="abs" style="left:144px;top:513px" width="32" height="32" viewBox="0 0 32 32" fill="none" stroke="#fff" stroke-width="2"><circle cx="16" cy="16" r="14.5"/><path d="M11 11l10 10M21 11L11 21" stroke-width="2.6"/></svg>
</section>

<!-- Music -->
<section class="screen music" style="left:1035px;top:1196px">
  <div class="title">Music</div>
  <div class="card" style="left:22px;top:68px;line-height:1.2">Manage<br>MP3<div class="card-img" role="img" aria-label="Music file image">Device IMG<small>To be Updated</small></div></div>
  <div class="card" style="left:168px;top:68px;line-height:1.2">Manage<br>Playlist<div class="card-img" role="img" aria-label="Playlist image">Device IMG<small>To be Updated</small></div></div>
  <nav class="nav"><div class="nav-item"><i></i>Home</div><div class="nav-item"><i></i>Add Device</div><div class="nav-item active"><i></i>Music</div></nav>
</section>

<!-- Manage Playlist -->
<section class="screen manage-playlist" style="left:1370px;top:1196px">
  <div class="title"><svg viewBox="0 0 14 14" fill="none" stroke="#666" stroke-width="2"><path d="M10 1L4 7l6 6"/></svg>Manage Playlist</div>
  <div class="tile" style="left:40px;top:89px"><div class="art"></div><b>+ Create New</b></div>
  <div class="tile" style="left:181px;top:89px"><div class="art"></div>Playlist Name</div>
  <div class="tile" style="left:40px;top:251px"><div class="art"></div>Playlist Name</div>
</section>

</div>
</body>
</html>
```